Industrial Automation company requires a business card design

Valtrin Automation provides design & build of Automated Equipment for manufacturing industry.
www.valtrinautomation.example
The equipment we design is used for manufacturing in sectors such as medical device, pharmaceutical, aerospace and electronics.
We require a new business card design which incorporates our (New) logo and the key message words:
Automated Equipment:
Design, Build, Control, Test, Support

```html
<!DOCTYPE html>
<html lang="en">
<head>
<meta charset="utf-8">
<title>Valtrin Automation – Business Card</title>
<link rel="stylesheet" href="https://fonts.googleapis.com/css2?family=Roboto:wght@300;400;500&display=swap">
<style>
  :root {
    --bg: #ece9e4;
    --card-white: #fbfbfb;
    --green: #4fae2f;
    --green-light: #8fd26a;
    --green-dark: #3a9a22;
    --brand-green: #4dbb8a;
    --ink: #555555;
    --ink-soft: #777777;
    --white: #ffffff;
  }
  * { box-sizing: border-box; margin: 0; padding: 0; }
  html, body { width: 1200px; height: 1023px; overflow: hidden; }
  body {
    background: var(--bg);
    font-family: "Roboto", sans-serif;
    position: relative;
  }
  .card {
    position: absolute;
    left: 250px;
    width: 700px;
    height: 400px;
    border-radius: 18px;
    overflow: hidden;
    box-shadow: 0 10px 30px rgba(0,0,0,0.18);
  }
  /* Front */
  .card-front { top: 80px; background: var(--card-white); }
  .front-content {
    position: absolute; left: 48px; top: 44px; bottom: 36px; right: 90px;
    display: flex; flex-direction: column;
  }
  .card-front .edge-band {
    position: absolute; right: 0; top: 0; bottom: 0; width: 46px;
    background: var(--green);
  }
  .edge-band .web {
    position: absolute; left: 50%; top: 50%;
    transform: translate(-50%, -50%) rotate(-90deg);
    color: var(--white); font-size: 15px; letter-spacing: 1px; white-space: nowrap;
  }
  .brand { display: flex; align-items: center; gap: 12px; }
  .brand-dot { width: 22px; height: 22px; border-radius: 50%; background: var(--brand-green); flex: none; }
  .brand-name {
    color: var(--brand-green); font-weight: 500; font-size: 30px; letter-spacing: 3px;
    text-transform: uppercase; white-space: nowrap;
  }
  .person { margin-top: 34px; }
  .person-name { color: var(--brand-green); font-size: 34px; font-weight: 300; line-height: 40px; }
  .person-title { color: var(--ink-soft); font-size: 17px; line-height: 22px; margin-top: 2px; }
  .contact {
    margin-top: auto;
    list-style: none; color: var(--ink); font-size: 16px; line-height: 26px;
  }
  .contact li { display: flex; align-items: center; gap: 10px; }
  .contact .ico { width: 16px; height: 16px; flex: none; }
  .contact .no-ico { padding-left: 26px; }
  /* Back */
  .card-back {
    top: 543px;
    background: radial-gradient(circle at 62% 42%, var(--green-light), var(--green) 55%, var(--green-dark));
    color: var(--white);
  }
  .back-brand {
    position: absolute; left: 0; right: 0; top: 110px;
    display: flex; align-items: center; justify-content: center; gap: 14px;
  }
  .back-brand .brand-dot { background: var(--white); width: 26px; height: 26px; }
  .back-brand .brand-name { color: var(--white); font-size: 44px; letter-spacing: 5px; }
  .tagline {
    position: absolute; left: 0; right: 0; top: 220px; text-align: center;
    font-size: 24px; font-weight: 400;
  }
  .services {
    position: absolute; left: 0; right: 0; top: 264px; text-align: center;
    font-size: 18px; letter-spacing: 0.5px;
  }
</style>
</head>
<body>
  <section class="card card-front" aria-label="Business card front">
    <div class="front-content">
      <div class="brand">
        <span class="brand-dot"></span>
        <span class="brand-name">Valtrin Automation</span>
      </div>
      <div class="person">
        <div class="person-name">Your Name</div>
        <div class="person-title">Title</div>
      </div>
      <ul class="contact">
        <li class="no-ico">Your Address</li>
        <li class="no-ico">in Just Two Line</li>
        <li>
          <svg class="ico" viewBox="0 0 16 16"><circle cx="8" cy="8" r="7" fill="none" stroke="#4fae2f" stroke-width="1.5"/><path d="M5.5 4.5l1.5 0 .8 2-1 .8a5 5 0 0 0 2 2l.8-1 2 .8v1.5c-3.5.3-6.4-2.6-6.1-6.1z" fill="#4fae2f"/></svg>
          55-010-48210
        </li>
        <li>
          <svg class="ico" viewBox="0 0 16 16"><rect x="4" y="1" width="8" height="14" rx="1.5" fill="none" stroke="#4fae2f" stroke-width="1.5"/><circle cx="8" cy="12.5" r="0.9" fill="#4fae2f"/></svg>
          55-010-48299
        </li>
        <li>
          <svg class="ico" viewBox="0 0 16 16"><rect x="1" y="3" width="14" height="10" fill="#4fae2f"/><path d="M1 3l7 6 7-6" fill="none" stroke="#fff" stroke-width="1.3"/></svg>
          info@valtrinautomation.example
        </li>
      </ul>
    </div>
    <div class="edge-band"><span class="web">www.valtrinautomation.example</span></div>
  </section>

  <section class="card card-back" aria-label="Business card back">
    <div class="back-brand">
      <span class="brand-dot"></span>
      <span class="brand-name">Valtrin Automation</span>
    </div>
    <p class="tagline">— Automated Equipment —</p>
    <p class="services">• Design • Build • Control • Test • Support</p>
  </section>
</body>
</html>
```